Tech business card design

We need an amazing business card design for our new business 'Brakka' a marketing tech startup based in Sydney, Australia. We provide an online marketplace for businesses to search and buy advertising media, connect with service providers and learn more about marketing. We wish to communicate 'cool tech', reliability and professionalism and design based around our logo.

Target Market(s)

Business Owners

Contact Information for Business Card

Name
Position
Email Address
Website
Phone Number

Font styles to use
Other font styles liked:
• Avenir & Avenir Next

Colors

Designer to choose colors to be used in the design.

```html
<!DOCTYPE html>
<html lang="en">
<head>
<meta charset="UTF-8">
<title>Brakka — Business Card</title>
<link rel="stylesheet" href="https://fonts.googleapis.com/css2?family=Nunito+Sans:wght@400;600;800&display=swap">
<style>
  :root {
    --navy: #14123f;
    --white: #ffffff;
    --paper-bg: #e9eaec;
    --faint-navy: #27255a;
    --muted: #c9c9dd;
    --shadow: rgba(20, 18, 63, 0.18);
  }
  * { box-sizing: border-box; margin: 0; padding: 0; }
  html, body {
    width: 1200px;
    height: 1000px;
    overflow: hidden;
    background: var(--paper-bg);
    font-family: "Nunito Sans", "Avenir Next", Avenir, sans-serif;
  }
  .canvas {
    position: relative;
    width: 1200px;
    height: 1000px;
  }
  .card {
    position: absolute;
    left: 280px;
    width: 640px;
    height: 366px;
    overflow: hidden;
    box-shadow: 0 14px 30px var(--shadow);
  }
  .card-front { top: 100px; background: var(--white); }
  .card-back  { top: 530px; background: var(--navy); }

  /* front */
  .info-panel {
    position: absolute;
    top: 0; right: 0;
    width: 300px; height: 366px;
    background: var(--navy);
    color: var(--white);
    padding: 40px 0 0 40px;
  }
  .panel-notch {
    position: absolute;
    top: 44px; left: 333px;
    width: 14px; height: 14px;
    border-radius: 50%;
    background: var(--white);
    border: 3px solid var(--navy);
  }
  .person-name {
    font-size: 21px;
    font-weight: 400;
    letter-spacing: 1px;
    text-transform: uppercase;
  }
  .person-title {
    margin-top: 4px;
    font-size: 10px;
    letter-spacing: 1.5px;
    color: var(--muted);
    text-transform: uppercase;
  }
  .contact-list {
    list-style: none;
    margin-top: 118px;
  }
  .contact-item {
    display: flex;
    align-items: center;
    gap: 10px;
    font-size: 13px;
    margin-bottom: 9px;
    letter-spacing: 0.3px;
  }
  .contact-icon { width: 14px; height: 14px; flex: none; }
  .wordmark-front {
    position: absolute;
    left: 38px; bottom: 72px;
    font-size: 82px;
    font-weight: 800;
    color: var(--navy);
    letter-spacing: -2px;
    line-height: 1;
  }

  /* back */
  .wordmark-faint {
    position: absolute;
    left: -20px; top: 60px;
    font-size: 230px;
    font-weight: 800;
    color: var(--faint-navy);
    letter-spacing: -6px;
    line-height: 1;
    white-space: nowrap;
  }
  .wordmark-back {
    position: absolute;
    left: 50%; top: 50%;
    transform: translate(-50%, -50%);
    font-size: 64px;
    font-weight: 800;
    color: var(--white);
    letter-spacing: -1.5px;
    line-height: 1;
  }
</style>
</head>
<body>
<main class="canvas">
  <section class="card card-front" aria-label="Business card front">
    <div class="wordmark-front">brakka</div>
    <div class="info-panel">
      <h1 class="person-name">Mara Lindqvist</h1>
      <p class="person-title">Owner/CEO</p>
      <ul class="contact-list">
        <li class="contact-item">
          <svg class="contact-icon" viewBox="0 0 24 24" aria-hidden="true"><path fill="#fff" d="M6.6 10.8a15.1 15.1 0 0 0 6.6 6.6l2.2-2.2a1 1 0 0 1 1-.25 11.4 11.4 0 0 0 3.6.57 1 1 0 0 1 1 1V20a1 1 0 0 1-1 1A17 17 0 0 1 3 4a1 1 0 0 1 1-1h3.5a1 1 0 0 1 1 1c0 1.25.2 2.45.57 3.57a1 1 0 0 1-.25 1z"/></svg>
          555.018.2741
        </li>
        <li class="contact-item">
          <svg class="contact-icon" viewBox="0 0 24 24" aria-hidden="true"><rect x="2" y="5" width="20" height="14" fill="#fff"/><path d="M2 5l10 8 10-8" fill="none" stroke="#14123f" stroke-width="2"/></svg>
          mara.lindqvist@brakka.com
        </li>
        <li class="contact-item">
          <svg class="contact-icon" viewBox="0 0 24 24" aria-hidden="true"><circle cx="12" cy="12" r="11" fill="#fff"/><g fill="none" stroke="#14123f" stroke-width="1.5"><circle cx="12" cy="12" r="7"/><ellipse cx="12" cy="12" rx="3" ry="7"/><path d="M5 12h14"/></g></svg>
          www.brakka.com
        </li>
      </ul>
    </div>
    <span class="panel-notch" aria-hidden="true"></span>
  </section>

  <section class="card card-back" aria-label="Business card back">
    <div class="wordmark-faint" aria-hidden="true">brakka</div>
    <div class="wordmark-back">brakka</div>
  </section>
</main>
</body>
</html>
```